Velora "Glass Tide" single cover

We need a cover for Velora's New upcoming single "Glass Tide"
We have posted some Pictures and logo that we want you to work With. We need you to get her to look good :).The title is "Glass Tide" and is "Velora feat. Dorvo mint rascal"
The songs is a little hiphop/RnB (Marla Q'ish).
You can choose what colour you want for the logo and overall. But we don't want it to be gloomy.
watch www.velora-music.example or www.facebook.com/veloramusic
This is a digital release so we need only front page 12x12cm
Updates
If anyone wants to remove the background from the pictures and be creative that is fine! :)
Industry/Entity Type
Digital
Colors
Designer to choose colors to be used in the design.
Look and feel
Each slider illustrates characteristics of the customer's brand and the style your logo design should communicate.

```html
<!DOCTYPE html>
<html lang="en">
<head>
<meta charset="utf-8">
<title>Velora "Glass Tide" single cover</title>
<link rel="stylesheet" href="https://fonts.googleapis.com/css2?family=Orbitron:wght@600;700&family=Russo+One&family=Arimo&display=swap">
<style>
  :root {
    --page-light: #ffffff;
    --page-edge: #d4d4d4;
    --band-black: #0b0b0b;
    --caption-text: #e8e8e8;
    --cover-frame: #ffffff;
    --cover-dark: #1a0f0a;
    --fire-core: #fff6c4;
    --fire-glow: #ffb52e;
    --fire-deep: #c2520e;
    --ember: #5a2410;
    --brick: #7a2e22;
    --photo-hair: #4a2c1c;
    --photo-dress: #1c1410;
    --logo-gold: #f6c445;
    --title-orange: #f4a019;
    --subtitle-orange: #f29a12;
  }
  * { margin: 0; padding: 0; box-sizing: border-box; }
  html, body {
    width: 1200px;
    height: 848px;
    overflow: hidden;
  }
  .canvas {
    position: relative;
    width: 1200px;
    height: 848px;
    background: radial-gradient(ellipse at 50% 45%, var(--page-light) 0%, #f2f2f2 45%, var(--page-edge) 100%);
  }
  .corner-band {
    position: absolute;
    left: 0;
    top: 0;
  }
  .cover {
    position: absolute;
    left: 318px;
    top: 122px;
    width: 566px;
    height: 566px;
    border: 3px solid var(--cover-frame);
    overflow: hidden;
    background: var(--cover-dark);
    box-shadow: 2px 3px 6px rgba(0,0,0,0.45);
  }
  .cover-artwork {
    position: absolute;
    inset: 0;
    background:
      radial-gradient(circle at 12% 30%, var(--fire-core) 0%, var(--fire-glow) 10%, rgba(244,140,30,0.6) 26%, rgba(0,0,0,0) 46%),
      radial-gradient(circle at 16% 82%, rgba(255,190,60,0.85) 0%, rgba(220,110,20,0.5) 22%, rgba(0,0,0,0) 42%),
      radial-gradient(ellipse at 88% 70%, rgba(60,40,30,0.9) 0%, rgba(20,14,10,0.8) 40%, rgba(0,0,0,0) 70%),
      linear-gradient(90deg, var(--fire-deep) 0%, #8a3a14 30%, var(--brick) 55%, #5a2a1c 80%, #2a1a14 100%);
  }
  .artist-photo {
    position: absolute;
    left: 150px;
    top: 10px;
    width: 300px;
    height: 470px;
    border-radius: 45% 45% 20% 20%;
    background:
      radial-gradient(ellipse at 48% 18%, rgba(210,160,130,0.85) 0%, rgba(150,95,60,0.7) 14%, rgba(0,0,0,0) 30%),
      radial-gradient(ellipse at 45% 30%, var(--photo-hair) 0%, rgba(74,44,28,0.8) 30%, rgba(0,0,0,0) 55%),
      linear-gradient(180deg, rgba(40,26,18,0.2) 0%, var(--photo-dress) 55%, rgba(28,20,16,0.6) 100%);
    filter: blur(4px);
  }
  .cover-text {
    position: absolute;
    left: 0;
    right: 0;
    text-align: center;
  }
  .artist-name {
    top: 330px;
    font-family: "Orbitron", sans-serif;
    font-weight: 700;
    font-size: 92px;
    line-height: 1;
    letter-spacing: 2px;
    color: var(--logo-gold);
  }
  .single-title {
    top: 459px;
    font-family: "Orbitron", sans-serif;
    font-weight: 600;
    font-size: 24px;
    line-height: 1;
    letter-spacing: 5px;
    color: var(--title-orange);
    text-transform: uppercase;
  }
  .credits {
    top: 491px;
    font-family: "Russo One", sans-serif;
    font-size: 14px;
    line-height: 1;
    letter-spacing: 0.3px;
    color: var(--subtitle-orange);
    text-transform: uppercase;
  }
  .caption-bar {
    position: absolute;
    left: 0;
    bottom: 0;
    width: 1200px;
    height: 56px;
    background: var(--band-black);
    display: flex;
    align-items: center;
    padding-left: 62px;
  }
  .caption {
    font-family: "Arimo", sans-serif;
    font-size: 16px;
    color: var(--caption-text);
  }
</style>
</head>
<body>
  <main class="canvas">
    <svg class="corner-band" width="240" height="110" viewBox="0 0 240 110" aria-hidden="true">
      <polygon points="0,68 0,102 226,0 172,0" fill="var(--band-black)"/>
    </svg>
    <section class="cover">
      <div class="cover-artwork" role="img" aria-label="Red brick wall bathed in glowing orange fire light, lens flares and dark swirling smoke"></div>
      <div class="artist-photo" role="img" aria-label="Photo of the singer with long wavy hair in a dark top, seated against the brick wall"></div>
      <h1 class="cover-text artist-name">Velora</h1>
      <h2 class="cover-text single-title">Glass Tide</h2>
      <p class="cover-text credits">Velora feat. Dorvo mint rascal</p>
    </section>
    <footer class="caption-bar">
      <p class="caption">Velora "Glass Tide" single cover</p>
    </footer>
  </main>
</body>
</html>
```